Veromar Cargo Flower trade show brochure

We are an international freight forwarding company from South America specialising in perishable handling both through air freight and sea freight. We need a brochure to hand out to customers in the flower fair trade shows in which we participate - China, Holland, Russia, USA. We need something clean yet striking and modern emphasising our brand and with great emphasis on our strengths in the perishable/flower forwarding realm. Our company is a merger of 4 of the largest forwarders in Ecuador into one company called Veromar Cargo Group. We would like emphasis on the new brand, however we do require that each individual logo of the 4 companies is portrayed in some way in the brochure. We are also registered with a global freight forwarding association known as PNQ which also must be mentioned. We would like a defined concept for perishable handling, something along the lines of (but not limited to) - first class travel - dont your flowers deserve the same ? Attached a JPEG file with our new website proposed design so that you have an idea of our tastes. Also attached is some basic text which can be used to put together the brochure. We would like some emphasis also on some fast data facts such as - 1. We ship to over 80 countries worldwide 2. we forward over 5000 tons of flowers per month 3. we track and trace over 150 shipments per day etc etc. Please also include our website adress - www.veromarcargo, and something along the lines of - Follow us on (logo Connectry), (logo Friendloop), logo (chirpnet) and our contact email address - info@veromarcargo.example

Target Market(s)

Flower importers worldwide

Industry/Entity Type

Freight Forwarding

Font styles to use
Sans Serif

Colors
9bcb3b
acd036
9d9d9d
757575

Requirements
Must have
• Photos of freight forwarding concepts, cut flowers

```html
<!DOCTYPE html>
<html lang="en">
<head>
<meta charset="utf-8">
<title>Veromar Cargo Group — Back Cover</title>
<link rel="stylesheet" href="https://fonts.googleapis.com/css2?family=Roboto:wght@300;400;500&display=swap">
<style>
  :root {
    --charcoal: #59595b;
    --leaf: #88bb41;
    --paper: #ffffff;
    --ink-light: #e4e4e4;
    --brand-grey: #4a4a4c;
  }
  * { margin: 0; padding: 0; box-sizing: border-box; }
  html, body { width: 1200px; height: 847px; overflow: hidden; }
  body { background: var(--charcoal); font-family: "Roboto", Arial, sans-serif; }
  .back-cover { position: relative; width: 1200px; height: 847px; overflow: hidden; background: var(--charcoal); }
  .diagonal-band { position: absolute; inset: 0; width: 1200px; height: 847px; }
  .diagonal-band polygon { fill: var(--leaf); }
  .brand-plate {
    position: absolute; left: 746px; top: 69px; width: 353px; height: 89px;
    background: var(--paper);
    display: flex; align-items: center; justify-content: center; gap: 14px;
  }
  .brand-plate .brand-name {
    font-weight: 500; font-size: 27px; color: var(--brand-grey); letter-spacing: -0.3px;
  }
  .brand-plate .brand-mark { width: 34px; height: 34px; background: var(--leaf); }
  .contact-list { position: absolute; left: 65px; top: 532px; color: var(--ink-light); font-weight: 300; }
  .contact-item { margin-bottom: 24px; }
  .contact-item dt { font-size: 19px; line-height: 24px; text-transform: uppercase; }
  .contact-item dd { font-size: 19px; line-height: 24px; }
  .social { position: absolute; left: 930px; top: 720px; width: 185px; text-align: center; color: var(--paper); }
  .social-title { font-size: 16px; font-weight: 300; margin-bottom: 14px; }
  .social-links { list-style: none; display: flex; justify-content: center; gap: 10px; font-size: 13px; font-weight: 400; }
</style>
</head>
<body>
  <main class="back-cover">
    <svg class="diagonal-band" viewBox="0 0 1200 847" aria-hidden="true">
      <polygon points="0,0 1200,0 1200,550 0,65"/>
    </svg>

    <div class="brand-plate">
      <span class="brand-name">Veromar Cargo Group</span>
      <span class="brand-mark" aria-hidden="true"></span>
    </div>

    <dl class="contact-list">
      <div class="contact-item"><dt>Address</dt><dd>Your address goes here, state, postcode, country</dd></div>
      <div class="contact-item"><dt>Contact</dt><dd>(+1) 123 -&nbsp; 567 - 890</dd></div>
      <div class="contact-item"><dt>Email</dt><dd>info@veromarcargo.example</dd></div>
      <div class="contact-item"><dt>Website</dt><dd>www.veromarcargo.com</dd></div>
    </dl>

    <div class="social">
      <p class="social-title">Like us on</p>
      <ul class="social-links">
        <li>Friendloop</li>
        <li>chirpnet</li>
        <li>Connectry</li>
      </ul>
    </div>
  </main>
</body>
</html>
```